Dorsey K. Wendell Business Card

We need a business card for our company Dorsey K. Wendell Heating & Plumbing to be distributed to potential customers. It should follow the color scheme of our logo and have a modern upscale and masculine look.

The logo is attached and the info below should also be included:

5187 W. Cedar Brook Rd.
Larkfield, PA 19650

Russell T. Wendell
(555) 592-0817
russelltwendell@fernmail.net
dorseykwendell.net
PA #093148

Industry/Entity Type

Business

Contact Information for Business Card

5187 W. Cedar Brook Rd.
Larkfield, PA 19650

Russell T. Wendell
(555) 592-0817
russelltwendell@fernmail.net
dorseykwendell.net
PA #093148

Colors

Designer to choose colors to be used in the design.

Requirements
Must have
• Information above included

```html
<!DOCTYPE html>
<html lang="en">
<head>
<meta charset="utf-8">
<title>Dorsey K. Wendell Business Card</title>
<link rel="stylesheet" href="https://fonts.googleapis.com/css2?family=Lato:wght@400;700;900&display=swap">
<style>
  :root {
    --brand-blue: #0a6fc2;
    --brand-blue-deep: #0857a3;
    --brand-green: #8cc63f;
    --card-white: #f7f7f5;
    --stage: #e6e8eb;
    --ink-white: #ffffff;
  }
  * { box-sizing: border-box; margin: 0; padding: 0; }
  html, body { width: 1200px; height: 780px; overflow: hidden; }
  body {
    background: var(--stage);
    font-family: "Lato", Arial, sans-serif;
    display: flex;
    align-items: center;
    justify-content: center;
    gap: 40px;
  }
  .card {
    position: relative;
    width: 540px;
    height: 309px;
    overflow: hidden;
    box-shadow: 0 6px 18px rgba(0,0,0,0.18);
  }

  /* Front */
  .card-front { background: var(--card-white); }
  .front-wordmark {
    position: absolute;
    left: 26px;
    top: 34px;
    width: 330px;
    color: var(--brand-blue);
    font-weight: 900;
    text-transform: uppercase;
    line-height: 1;
  }
  .front-wordmark .wordmark-name { display: block; font-size: 28px; letter-spacing: 0.3px; white-space: nowrap; }
  .front-wordmark .wordmark-trade { display: block; font-size: 13px; letter-spacing: 2px; margin-top: 9px; white-space: nowrap; }
  .brand-square {
    position: absolute;
    right: 34px;
    top: 22px;
    width: 128px;
    height: 128px;
    border: 14px solid var(--brand-blue);
    background: var(--card-white);
  }
  .accent-rule {
    position: absolute;
    left: 0;
    top: 138px;
    width: 378px;
    height: 3px;
    background: var(--brand-green);
  }
  .contact-band {
    position: absolute;
    left: 0;
    top: 146px;
    width: 378px;
    height: 116px;
    background: var(--brand-blue);
    color: var(--ink-white);
    padding: 14px 0 0 28px;
  }
  .contact-name { font-size: 19px; font-weight: 400; line-height: 1.1; }
  .contact-license { font-size: 12px; margin-top: 2px; letter-spacing: 0.5px; }
  .contact-list { list-style: none; margin-top: 8px; }
  .contact-list li {
    display: flex;
    align-items: center;
    gap: 7px;
    font-size: 12px;
    line-height: 1;
    margin-bottom: 5px;
  }
  .contact-icon { width: 13px; height: 13px; flex: none; }
  .address-strip {
    position: absolute;
    left: 0;
    bottom: 0;
    width: 100%;
    height: 34px;
    background: var(--brand-green);
    color: var(--ink-white);
    font-size: 12.5px;
    display: flex;
    align-items: center;
    justify-content: flex-end;
    padding-right: 24px;
    letter-spacing: 0.3px;
  }

  /* Back */
  .card-back {
    background: linear-gradient(160deg, var(--brand-blue) 0%, var(--brand-blue-deep) 100%);
    display: flex;
    align-items: center;
    justify-content: center;
    gap: 18px;
  }
  .back-square {
    width: 58px;
    height: 58px;
    border: 7px solid var(--ink-white);
  }
  .back-wordmark {
    color: var(--ink-white);
    font-weight: 900;
    text-transform: uppercase;
    line-height: 1;
  }
  .back-wordmark .wordmark-name { display: block; font-size: 28px; letter-spacing: 0.3px; white-space: nowrap; }
  .back-wordmark .wordmark-trade { display: block; font-size: 13px; letter-spacing: 2px; margin-top: 8px; white-space: nowrap; }
  .back-rule { width: 100%; height: 2px; background: var(--brand-green); margin-top: 6px; }
</style>
</head>
<body>
  <section class="card card-front">
    <div class="front-wordmark">
      <span class="wordmark-name">Dorsey K. Wendell</span>
      <span class="wordmark-trade">Heating &amp; Plumbing</span>
    </div>
    <div class="brand-square"></div>
    <div class="accent-rule"></div>
    <div class="contact-band">
      <p class="contact-name">Russell T. Wendell</p>
      <p class="contact-license">PA #093148</p>
      <ul class="contact-list">
        <li>
          <svg class="contact-icon" viewBox="0 0 16 16" aria-hidden="true"><circle cx="8" cy="8" r="7.5" fill="#fff"/><path d="M5.2 4.2l1.4-.2.8 2-1 .8a5.5 5.5 0 0 0 2.8 2.8l.8-1 2 .8-.2 1.4c-3.8.4-7-2.8-6.6-6.6z" fill="#0a6fc2"/></svg>
          (555) 592-0817
        </li>
        <li>
          <svg class="contact-icon" viewBox="0 0 16 16" aria-hidden="true"><circle cx="8" cy="8" r="7.5" fill="#fff"/><rect x="4" y="5.2" width="8" height="5.6" fill="none" stroke="#0a6fc2" stroke-width="1.2"/><path d="M4 5.4l4 3 4-3" fill="none" stroke="#0a6fc2" stroke-width="1.2"/></svg>
          russelltwendell@fernmail.net
        </li>
        <li>
          <svg class="contact-icon" viewBox="0 0 16 16" aria-hidden="true"><circle cx="8" cy="8" r="7.5" fill="#fff"/><circle cx="8" cy="8" r="4.2" fill="none" stroke="#0a6fc2" stroke-width="1.1"/><ellipse cx="8" cy="8" rx="1.8" ry="4.2" fill="none" stroke="#0a6fc2" stroke-width="1.1"/><path d="M3.8 8h8.4" stroke="#0a6fc2" stroke-width="1.1"/></svg>
          dorseykwendell.net
        </li>
      </ul>
    </div>
    <div class="address-strip">5187 W. Cedar Brook Rd. Larkfield, PA 19650</div>
  </section>

  <section class="card card-back">
    <div class="back-square"></div>
    <div class="back-wordmark">
      <span class="wordmark-name">Dorsey K. Wendell</span>
      <div class="back-rule"></div>
      <span class="wordmark-trade">Heating &amp; Plumbing</span>
    </div>
  </section>
</body>
</html>
```